Marrowind Leaf range - labels for a range of teas.

Our company name is Marrowind Leaf Company - based in Melbourne, Australia. We have a current logo project with Pixel Harbor.

We offer a range of top quality teas - black, green, white, oolongs, herbals, flavoured teas. From Japan, Assam, Darjeeling, Ceylon, Africa and elsewhere. The very best loose teas, and some pyramid tea bags too.

We cover some blends : English Breakfast, African Breakfast, Ceylon Breakfast, Earl Grey amongst them.

And herbal variants: lemon grass and ginger, chamomile, peppermint, rooibos and chilli.

And fruit teas.... and flavoured teas like vanilla, peach and raspberry.

We aim to occupy a modern, contemporary, sophisticated and global space.... but we can be funky too, especially with the fruit and herbal offers. Quality is paramount ! We do not aim to have the biggest range of teas, but we are very particular. And we source directly from origin.... fresh quality teas.

Would lean towards black teas being on a black background label, green teas on a green background, white etas on a white background, herbals maybe on a straw or suitable background, and flavoured teas on a specific background colour too....maybe fuschia? Violet ? But colourful is key.

The panel should indicate teas being Loose or Pyramid bags. And the nett weight should be shown.... Loose could be for example 75 gr, 125 gr 250 gr etc.. And pyramids would show the number of pyramids and weight, example 20 x Pyramids 50 gr
50 Pyramids 150 gr etc.

And 'Marrowind Leaves' or 'Marrowind Leaf Company' should be on the panel too. Melbourne can appear as well if it gels with the total look.

There will need to be 2 lines - in order or juxtaposed, doesn't matter - showing the origin and 'mark' and grade. Example being:
Ceylon
Kenwick Pekoe

or

Darjeeling
Melgara TGFOP1

or

China
Jasmine Leaf

We just need templates to cover the different types of tea - black, green, white, herbal, flavoured - as there are too many (and changing) types of tea in the range .

Any questions...please ask...

Thanks

Reason: Needs to have alater deadline than the current Logo Project associated with the same Marrowind Leaf Company start up.

Target Market(s)

Sophisticated. Real tea lovers. Discriminating tastes.

Industry/Entity Type

Weight

Font styles to use
Sans Serif

Requirements
Must have
• Sophisticated
Cool
Premium quality branding
Bold
Uber modern
Nice to have
• BOLD text.....
Cool fonts....
Pretty bold and minimalist - ultra modern if possible....uber modern
Bright colours and use of black and white..... Not really into pastels etc..

Lots of black colour too is a likely plus
Should not have
• Frilly stuff

```html
<!DOCTYPE html>
<html lang="en">
<head>
<meta charset="utf-8">
<title>Marrowind Leaf Co — Tea Label Range</title>
<link rel="stylesheet" href="https://fonts.googleapis.com/css2?family=Oswald:wght@400;500;600&display=swap">
<style>
  :root {
    --page: #ffffff;
    --black-tea: #2c2a33;
    --china-stone: #d4d8d0;
    --assam-teal: #1b4650;
    --cream: #efe5d3;
    --ceylon-green: #78a757;
    --ink-navy: #17202c;
    --jasmine-violet: #8c5cb9;
    --assam-green: #4fbd6e;
  }
  * { margin: 0; padding: 0; box-sizing: border-box; }
  html, body {
    width: 1200px;
    height: 807px;
    overflow: hidden;
    background: var(--page);
  }
  .range {
    position: relative;
    width: 1200px;
    height: 807px;
  }
  .label {
    position: absolute;
    top: 134px;
    width: 288px;
    height: 511px;
    display: flex;
    flex-direction: column;
    align-items: center;
    font-family: "Oswald", "Arial Narrow", sans-serif;
    text-align: center;
  }
  .label--ceylon { left: 151px; background: var(--black-tea); --name: var(--cream); --rule: var(--ceylon-green); --detail: var(--cream); --origin: var(--ceylon-green); --grade: var(--cream); }
  .label--china  { left: 463px; background: var(--china-stone); --name: var(--ink-navy); --rule: var(--jasmine-violet); --detail: var(--jasmine-violet); --origin: var(--ink-navy); --grade: var(--jasmine-violet); }
  .label--assam  { left: 766px; background: var(--assam-teal); --name: var(--cream); --rule: var(--assam-green); --detail: var(--cream); --origin: var(--assam-green); --grade: var(--cream); }

  .brand {
    margin-top: 84px;
    display: flex;
    flex-direction: column;
    align-items: center;
  }
  .brand__name {
    font-weight: 500;
    font-size: 19px;
    letter-spacing: 2.5px;
    line-height: 1;
    color: var(--name);
    text-transform: uppercase;
  }
  .brand__rule {
    width: 168px;
    height: 2px;
    margin-top: 9px;
    background: var(--rule);
  }
  .brand__city {
    margin-top: 6px;
    font-weight: 400;
    font-size: 9px;
    letter-spacing: 3px;
    color: var(--name);
    text-transform: uppercase;
  }
  .pack-size {
    margin-top: 30px;
    font-weight: 500;
    font-size: 24px;
    line-height: 1;
    color: var(--detail);
  }
  .origin {
    margin-top: 16px;
    font-weight: 500;
    font-size: 76px;
    line-height: 1;
    letter-spacing: -1px;
    color: var(--origin);
    text-transform: uppercase;
  }
  .grade {
    margin-top: 6px;
    font-weight: 500;
    font-size: 66px;
    line-height: 0.96;
    color: var(--grade);
  }
</style>
</head>
<body>
  <main class="range">
    <section class="label label--ceylon">
      <div class="brand">
        <span class="brand__name">Marrowind Leaf Co</span>
        <span class="brand__rule"></span>
        <span class="brand__city">Melbourne</span>
      </div>
      <p class="pack-size">20 x Pyramids 50 gr</p>
      <h2 class="origin">Ceylon</h2>
      <p class="grade">Kenwick<br>Pekoe</p>
    </section>

    <section class="label label--china">
      <div class="brand">
        <span class="brand__name">Marrowind Leaf Co</span>
        <span class="brand__rule"></span>
        <span class="brand__city">Melbourne</span>
      </div>
      <p class="pack-size">20 x Pyramids 50 gr</p>
      <h2 class="origin">China</h2>
      <p class="grade">Jasmine<br>Leaf</p>
    </section>

    <section class="label label--assam">
      <div class="brand">
        <span class="brand__name">Marrowind Leaf Co</span>
        <span class="brand__rule"></span>
        <span class="brand__city">Melbourne</span>
      </div>
      <p class="pack-size">20 x Pyramids 50 gr</p>
      <h2 class="origin">Assam</h2>
      <p class="grade">Kenwick<br>Pekoe</p>
    </section>
  </main>
</body>
</html>
```